Full service meeting planning company needs new business cards

Velmora Linkway is a full service meeting planning company that specializes in on-line conference registration web development and event communications. We combine citywide hotel management, mobile applications, eblast reminders, confirmation letters, and customized reporting to create a seamless registration process. We also manage group motor coach transportation, food and beverages, entertainment, stage and lighting for group of 10 to 4000.

Target Market(s)

Corporations and associations

Industry/Entity Type

Event Planning

Contact Information for Business Card

standard size 3.5" wide and 2" tall

Font styles to use
Serif
Sans Serif

Colors
f37122
f78f20
333333
5c5c5c
9d9d9d
f68d4d

Requirements
Must have
• {name}
• Velmora Linkway
• P.O. Box 7384, Brindle Falls, WA 98921
• www.velmoralinkway.com
• {email}
• {phone}
• {mobile phone}
Nice to have
• Our colors are black, grey and orange as an accent color
Should not have
• I am not happy with our website layout anymore either. It feels dark and old but it does explain who we are pretty well if you'd like to review; www.velmoralinkway.com

```html
<!DOCTYPE html>
<html lang="en">
<head>
<meta charset="utf-8">
<title>Velmora Linkway – Business Card</title>
<link rel="stylesheet" href="https://fonts.googleapis.com/css2?family=Jost:wght@400;500&family=Playfair+Display:wght@500&display=swap">
<style>
  :root{
    --orange:#f37122;
    --orange-light:#f78f20;
    --ink:#333333;
    --grey:#5c5c5c;
    --grey-light:#9d9d9d;
    --paper:#ffffff;
    --backdrop:#717675;
  }
  *{box-sizing:border-box;margin:0;padding:0}
  html,body{width:1200px;height:800px;overflow:hidden}
  body{background:var(--backdrop);font-family:"Jost",sans-serif;position:relative}

  .card{
    position:absolute;top:252px;width:520px;height:297px;
    background:var(--paper);overflow:hidden;
    box-shadow:0 6px 18px rgba(0,0,0,.25);
  }
  .card--back{left:40px}
  .card--front{left:640px}
  .card__band{
    position:absolute;left:0;right:0;bottom:16px;height:11px;
    background:linear-gradient(90deg,var(--orange),var(--orange-light));
  }

  /* front */
  .front-brand{
    position:absolute;left:46px;top:74px;display:flex;align-items:center;gap:18px;
  }
  .front-brand__disc{
    width:122px;height:122px;border-radius:50%;
    background:radial-gradient(circle at 35% 30%,var(--orange-light),var(--orange));
    flex:none;
  }
  .front-brand__name{
    color:var(--orange);font-size:28px;font-weight:500;letter-spacing:.04em;
    text-transform:uppercase;margin-top:40px;white-space:nowrap;
  }

  /* back */
  .holder{position:absolute;left:70px;top:56px;width:160px}
  .holder__name{
    font-family:"Playfair Display",serif;font-weight:500;font-size:40px;
    color:#111;line-height:1;
  }
  .holder__company{
    font-size:8.5px;letter-spacing:.06em;text-transform:uppercase;
    color:var(--ink);margin-top:4px;
  }
  .divider-v{position:absolute;left:238px;top:52px;width:1px;height:112px;background:var(--grey)}
  .divider-h{position:absolute;left:80px;top:180px;width:158px;height:1px;background:var(--grey)}

  .contact-list{position:absolute;left:258px;top:62px;list-style:none}
  .contact-list__item{
    display:flex;align-items:center;gap:10px;margin-bottom:12px;
    font-size:17px;color:var(--ink);
  }
  .contact-list__icon{
    width:25px;height:25px;border-radius:50%;background:var(--orange);
    display:flex;align-items:center;justify-content:center;flex:none;
  }

  .company-block{position:absolute;left:40px;top:190px;display:flex;align-items:center;gap:12px}
  .company-block__disc{width:70px;height:70px;border-radius:50%;background:var(--ink);flex:none}
  .company-block__text{font-size:9.5px;color:var(--grey);line-height:1.3}
  .company-block__name{font-size:11px;color:var(--ink);font-weight:500}
  .company-block__small{font-size:8px;color:var(--grey-light)}
</style>
</head>
<body>

  <section class="card card--back" aria-label="Business card back">
    <div class="holder">
      <p class="holder__name">Name</p>
      <p class="holder__company">Velmora Linkway</p>
    </div>
    <span class="divider-v"></span>
    <ul class="contact-list">
      <li class="contact-list__item">
        <span class="contact-list__icon">
          <svg width="13" height="13" viewBox="0 0 24 24" aria-hidden="true"><path fill="#fff" d="M6.6 10.8a15.1 15.1 0 0 0 6.6 6.6l2.2-2.2c.3-.3.7-.4 1-.2 1.1.4 2.3.6 3.6.6.6 0 1 .4 1 1V20c0 .6-.4 1-1 1A17 17 0 0 1 3 4c0-.6.4-1 1-1h3.5c.6 0 1 .4 1 1 0 1.3.2 2.5.6 3.6.1.3 0 .7-.2 1z"/></svg>
        </span>Phone
      </li>
      <li class="contact-list__item">
        <span class="contact-list__icon">
          <svg width="12" height="14" viewBox="0 0 12 18" aria-hidden="true"><rect x="1" y="1" width="10" height="16" rx="2" fill="none" stroke="#fff" stroke-width="1.6"/><circle cx="6" cy="14" r="1" fill="#fff"/></svg>
        </span>Phone Movile
      </li>
      <li class="contact-list__item">
        <span class="contact-list__icon">
          <svg width="13" height="10" viewBox="0 0 16 12" aria-hidden="true"><rect x="1" y="1" width="14" height="10" fill="none" stroke="#fff" stroke-width="1.5"/><path d="M1 1l7 6 7-6" fill="none" stroke="#fff" stroke-width="1.5"/></svg>
        </span>email
      </li>
    </ul>
    <span class="divider-h"></span>
    <div class="company-block">
      <span class="company-block__disc"></span>
      <div class="company-block__text">
        <p class="company-block__name">Velmora Linkway</p>
        <p>P.O. Box 7384</p>
        <p>Brindle Falls, WA 98921</p>
        <p class="company-block__small">www.velmoralinkway.com</p>
        <p class="company-block__small">(555) 555-0148</p>
      </div>
    </div>
    <span class="card__band"></span>
  </section>

  <section class="card card--front" aria-label="Business card front">
    <div class="front-brand">
      <span class="front-brand__disc"></span>
      <p class="front-brand__name">Velmora Linkway</p>
    </div>
    <span class="card__band"></span>
  </section>

</body>
</html>
```